Brightvarrow LLC - Engineering Consulting and Startup Incubation

Brightvarrow LLC is a fast paced, energetic startup incubator and engineering consulting company based in the greater Boston area. Our process includes bringing in clients with ideas for new products and services, and working with them to design and manufacture functional prototypes. We have a talented team of engineers capable of designing new technologies for the future, including electronics, mechanical systems, transportation systems, medical devices, and consumer products.

Our core values for design are:
Sustainability
Economical
Simplicity
Tasteful
Environmentally Friendly

We need an attractive website that can help us to convey our talents/capabilities, and help bring in new clients.
thanks!

Target Market(s)

Our target clientele includes scientific reasearchers, entrepreneurers and business professionals. Age range 20-50.

Industry/Entity Type

Medical

Requirements
Must have
• The website should consist of at least three main pages:
-A home page, including some preliminary information
-A 'capabilities' page, where pictures of past projects and our facilities can be displayed
-A 'contact us/submit your idea' page

Also the potential to add a more detailed 'about us' page where we can describe our history and team members profiles.
Nice to have
• Some limited level of interactivity.

```html
<!DOCTYPE html>
<html lang="en">
<head>
<meta charset="utf-8">
<title>Brightvarrow LLC</title>
<link rel="stylesheet" href="https://fonts.googleapis.com/css2?family=Arimo:wght@400;700&display=swap">
<style>
:root{
  --page:#e7e7e7;
  --panel:#ffffff;
  --ink:#111111;
  --body:#444444;
  --muted:#8a8a8a;
  --soft:#f1f1f1;
  --rule:#e0e0e0;
  --brand:#d9141b;
  --btn-top:#8a8a8a;
  --btn-bot:#5e5e5e;
}
*{box-sizing:border-box;margin:0;padding:0}
html,body{width:1200px;height:1173px;overflow:hidden}
body{background:var(--page);font-family:"Arimo",Arial,sans-serif;color:var(--body);position:relative}
a{color:inherit;text-decoration:none}

.site-header{position:absolute;left:90px;top:13px;width:1020px;height:187px;background:var(--panel);border-radius:0 0 6px 6px;box-shadow:0 6px 10px -6px rgba(0,0,0,.25)}
.brand{position:absolute;left:10px;top:30px;display:flex;align-items:center;gap:8px}
.brand-dot{width:40px;height:40px;border-radius:50%;background:var(--brand)}
.brand-word{position:relative;display:block}
.brand-name{display:block;font-size:27px;font-weight:700;color:var(--brand);letter-spacing:-.5px;line-height:1;white-space:nowrap}
.brand-suffix{position:absolute;right:0;top:31px;font-size:10px;color:var(--ink);font-weight:700}
.account-links{position:absolute;right:22px;top:22px;font-size:14px;color:var(--muted);letter-spacing:.3px}
.account-links .sep{margin:0 10px;font-size:10px;color:#bbb}
.call-us{position:absolute;left:628px;top:68px;font-size:19px;font-weight:700;color:#333}
.call-us strong{color:var(--brand)}
.search{position:absolute;left:842px;top:64px;width:169px;height:29px;border:1px solid #cfcfcf;font-size:11px;color:#333;padding:8px 12px}
.search svg{position:absolute;right:8px;top:6px}
.header-rule{position:absolute;left:10px;right:8px;top:117px;border-top:1px solid var(--rule)}
.main-nav{position:absolute;left:0;right:0;top:135px;height:52px;display:flex;background:linear-gradient(#fff,#ececec);border-radius:0 0 6px 6px}
.main-nav a{display:flex;align-items:center;justify-content:center;font-size:14.5px;font-weight:700;color:#444;border-right:1px solid #dcdcdc}
.main-nav a:last-child{border-right:0}
.main-nav .current{color:var(--brand);background:linear-gradient(#fff,#e4e4e4)}

.hero{position:absolute;left:0;top:210px;width:1200px;height:322px;background:radial-gradient(ellipse at 55% 50%,#fafafa,#e9e9e9 70%)}
.hero h1{position:absolute;left:185px;top:64px;font-size:33px;font-weight:700;color:#878787;white-space:nowrap}
.hero p{position:absolute;left:186px;top:118px;width:600px;font-size:13.5px;line-height:23px;color:#444}
.btn{position:absolute;top:203px;height:43px;display:flex;align-items:center;justify-content:space-between;padding:0 14px;background:linear-gradient(var(--btn-top),var(--btn-bot));border:1px solid #555;border-radius:3px;color:#fff;font-weight:700;font-size:16px;white-space:nowrap;box-shadow:0 2px 3px rgba(0,0,0,.25)}
.btn .chev{flex:none;width:18px;height:18px;border-radius:50%;background:#3f3f3f;display:flex;align-items:center;justify-content:center}
.btn-contact{left:188px;width:165px}
.btn-submit{left:373px;width:224px;color:#eee}
.slide-arrow{position:absolute;top:131px;width:42px;height:42px;border-radius:50%;background:#fbfbfb;box-shadow:0 1px 3px rgba(0,0,0,.25);display:flex;align-items:center;justify-content:center}
.slide-prev{left:90px}.slide-next{left:1068px}
.hero-art{position:absolute;left:845px;top:33px;width:157px;height:263px;border-radius:78px 78px 30px 30px;background:radial-gradient(circle at 45% 30%,#ffffff,#d2d2d2 65%,#9a9a9a)}

.content{position:absolute;left:90px;top:534px;width:1020px;height:532px;background:var(--panel);border-radius:6px 6px 0 0}
.content h2{font-size:22px;font-weight:700;color:var(--ink)}
.content h3{font-size:18px;font-weight:700;color:var(--ink)}
.text{font-size:13.3px;line-height:23px;color:#444;text-align:justify}
.welcome{position:absolute;left:10px;top:15px;width:695px}
.welcome .text{margin-top:9px}
.rule{position:absolute;left:10px;width:695px;border-top:1px solid var(--rule)}
.what{position:absolute;left:10px;top:231px;width:695px}
.what .text{width:461px;margin-top:13px}
.video{position:absolute;left:490px;top:266px;width:212px;height:126px;border-radius:4px;background:linear-gradient(135deg,#5a5f6a,#8c7a86 45%,#4a4e5a)}
.video .play{position:absolute;left:85px;top:42px;width:42px;height:42px;border-radius:50%;background:#dcdcdc;border:2px solid #f5f5f5;display:flex;align-items:center;justify-content:center}
.clients{position:absolute;left:11px;top:446px;font-size:13.5px;color:#222}
.client-row{position:absolute;left:20px;top:478px;width:680px;display:flex;justify-content:space-between;font-size:20px;font-weight:700;color:#333}

.projects{position:absolute;left:728px;top:0}
.projects h2{position:absolute;left:0;top:20px;font-size:18.5px;white-space:nowrap}
.project{position:absolute;left:-3px;width:285px;height:132px;background:var(--soft)}
.project .thumb{position:absolute;left:12px;top:10px;width:100px;height:111px;border:3px solid #fff;box-shadow:0 0 2px rgba(0,0,0,.3)}
.project p{position:absolute;left:127px;top:16px;width:147px;font-size:13.3px;line-height:19px;color:#444;text-align:justify}
.project .more{position:absolute;left:127px;top:100px;font-size:13px;color:var(--muted);font-weight:700}
.view-all{position:absolute;right:12px;top:498px;font-size:12.5px;font-weight:700;color:var(--muted)}
.view-all span{font-size:18px;margin-left:4px}

.site-footer{position:absolute;left:90px;top:1097px;width:1020px}
.footer-nav{font-size:12.5px;color:#333}
.footer-nav .sep{margin:0 8px}
.copyright{margin-top:17px;font-size:12.5px;color:#333}
.social{position:absolute;right:0;top:16px;display:flex;gap:10px;font-size:12px;font-weight:700;color:#444}
</style>
</head>
<body>

<header class="site-header">
  <div class="brand">
    <span class="brand-dot"></span>
    <span class="brand-word"><span class="brand-name">Brightvarrow</span><span class="brand-suffix">LLC</span></span>
  </div>
  <nav class="account-links"><a href="#">REGISTER</a><span class="sep">::</span><a href="#">LOGIN</a></nav>
  <div class="call-us">Call us : <strong>555 210 4836</strong></div>
  <div class="search">Search
    <svg width="16" height="16" viewBox="0 0 16 16"><circle cx="6" cy="6" r="4.5" fill="#222"/><line x1="9" y1="9" x2="14" y2="14" stroke="#222" stroke-width="3" stroke-linecap="round"/></svg>
  </div>
  <div class="header-rule"></div>
  <nav class="main-nav">
    <a href="#" class="current" style="width:160px">Home</a>
    <a href="#" style="width:193px">About us</a>
    <a href="#" style="width:222px">Capabilities</a>
    <a href="#" style="width:252px">Submit your idea</a>
    <a href="#" style="width:193px">Contact us</a>
  </nav>
</header>

<section class="hero">
  <h1>Sustainability, Economical, Simplicity</h1>
  <p>Cras lobortis viverra felis, fermentum condimentum lacus tempus in. Maecenas sollicitudin dui non ligula facilisis egestas. Cras in dictum libero. Etiam vitae dui in tellus ultricies feugiat quis non neque. Nunc nisl velit, rhoncus a faucibus at, sodales sed justo.</p>
  <a href="#" class="btn btn-contact">CONTACT US <span class="chev"><svg width="8" height="10" viewBox="0 0 8 10"><path d="M2 1l4 4-4 4" fill="none" stroke="#fff" stroke-width="1.8"/></svg></span></a>
  <a href="#" class="btn btn-submit">SUBMIT YOUR IDEA <span class="chev"><svg width="8" height="10" viewBox="0 0 8 10"><path d="M2 1l4 4-4 4" fill="none" stroke="#fff" stroke-width="1.8"/></svg></span></a>
  <a href="#" class="slide-arrow slide-prev" aria-label="Previous slide"><svg width="12" height="18" viewBox="0 0 12 18"><path d="M9 2L3 9l6 7" fill="none" stroke="#aaa" stroke-width="1.6"/></svg></a>
  <a href="#" class="slide-arrow slide-next" aria-label="Next slide"><svg width="12" height="18" viewBox="0 0 12 18"><path d="M3 2l6 7-6 7" fill="none" stroke="#aaa" stroke-width="1.6"/></svg></a>
  <div class="hero-art" role="img" aria-label="Glowing white light bulb"></div>
</section>

<main class="content">
  <section class="welcome">
    <h2>Welcome to our site</h2>
    <p class="text">Etiam eu nunc vitae mi dignissim sollicitudin ac nec eros. Aliquam id mauris tempor dolor sagittis aliquam. Suspend isse ullamcorper lectus sollicitudin quam consectetur accumsan. Integer tincidunt odio lorem, sodales cursus magna congue non. Suspendisse a tortor molestie, tincidunt eros in, porta arcu. Etiam orci enim, suscipit in nunc non, ultrices euismod magna. Maecenas vitae lacus mollis, suscipit erat nec, porta arcu. Nunc facilisis pulvinar metus congue ornare. Fusce dapibus mi sit amet nulla tempor lacinia. Nulla nec quam risus. Fusce sed suscipit nisl, nec auctor ante. Sed mi odio, cursus quis libero tincidunt, accumsan tincidunt justo.</p>
  </section>
  <div class="rule" style="top:208px"></div>
  <section class="what">
    <h3>What we do?</h3>
    <p class="text">Nunc a nisl consequat, accumsan ipsum a, fermentum enim. Class aptent taciti sociosqu ad litora torquent per conubia nostra, per inceptos hime naeos. Donec a purus non neque porta tincidunt. Suspendisse et rutrum elit. Quisque accumsan pretium lectus, quis volutpat metus semper et. Donec varius dapibus dolor, a vehicula orci fringilla at. Suspendisse vitae congue leo, non venenatis leoaugue tellus, eleifend vel.</p>
  </section>
  <div class="video" role="img" aria-label="Video still of a man painting colourful splashes on a wall">
    <span class="play"><svg width="14" height="16" viewBox="0 0 14 16"><path d="M2 1l11 7-11 7z" fill="#333"/></svg></span>
  </div>
  <div class="rule" style="top:428px"></div>
  <p class="clients">Clients</p>
  <div class="client-row">
    <span>Greenbasket</span><span>Searchly</span><span>Linkwise</span><span>Ledgerly</span><span>Kyomark</span><span>Telvane</span>
  </div>

  <aside class="projects">
    <h2>Our Past Projects</h2>
    <article class="project" style="top:58px">
      <div class="thumb" role="img" aria-label="Businesswoman with folded arms" style="background:linear-gradient(#d8dadc,#8b8e92)"></div>
      <p>Duis aliquet est a blandit fermentum nec elemen tum libero lanta rutrum ultrices semper.</p>
      <a href="#" class="more">VIEW MORE</a>
    </article>
    <article class="project" style="top:205px">
      <div class="thumb" role="img" aria-label="Two people thinking in front of a chalkboard" style="background:linear-gradient(#3a3d40,#6b6a68)"></div>
      <p>Duis aliquet est a blandit fermentum nec elemen tum libero lanta rutrum ultrices semper.</p>
      <a href="#" class="more">VIEW MORE</a>
    </article>
    <article class="project" style="top:351px">
      <div class="thumb" role="img" aria-label="Businessman pointing up at a light bulb" style="background:linear-gradient(#2c3e4e,#5d6f7c)"></div>
      <p>Duis aliquet est a blandit fermentum nec elemen tum libero lanta rutrum ultrices semper.</p>
      <a href="#" class="more">VIEW MORE</a>
    </article>
  </aside>
  <a href="#" class="view-all">VIEW ALL PAST PROJECTS<span>»</span></a>
</main>

<footer class="site-footer">
  <nav class="footer-nav"><a href="#">Home</a><span class="sep">|</span><a href="#">About Us</a><span class="sep">|</span><a href="#">Capabilities</a><span class="sep">|</span><a href="#">Submit your idea</a><span class="sep">|</span><a href="#">Contact us</a></nav>
  <p class="copyright">Copyright &nbsp;©&nbsp; 2013 &nbsp;Brightvarrow. &nbsp;&nbsp;All rights reserved.</p>
  <div class="social"><a href="#">Friendhub</a><a href="#">Chirpwire</a></div>
</footer>

</body>
</html>
```